Wander Glade Journeys Stationary
Business card, envelopes and letterhead layout
Please add business cards for these people to design 106 in the same format. They do not mailing address information or separate cell phone.
Nora Pell Travel Consultant
nora.pell@wanderglade.example
Glen Ashby Marketing Director
glen.ashby@wanderglade.example
Tessa Vandrunen Travel Consultant
tessa.vandrunen@wanderglade.example
Megan Tully Travel Consultant
megan.tully@wanderglade.example
Jodi Farley Travel Consultant
jodi.farley@wanderglade.example
For the phone and cell numbers, please have the phone number have punctuation. When I submitted the brief it made me take it out. Should be 555.204.7719 and 555.316.8245
I am liking the designs. I don't want to incorporate the darker red color into the design. I like the shadowed look of the logo in the designs by vespiq. Is that meant to be on the back?
I would like to have designs for letterhead, envelopes, business cards and email signature.
I have decided I would like to have 2 sided business cards. On the back,
Where can we take you?
Honeymoons
Destination Weddings
Family Travel
Celebration Vacations

```html
<!DOCTYPE html>
<html lang="en">
<head>
<meta charset="utf-8">
<title>Wander Glade Journeys Stationery</title>
<link href="https://fonts.googleapis.com/css2?family=Pacifico&family=Open+Sans:wght@400;600&display=swap" rel="stylesheet">
<style>
  :root{
    --bg:#ece6dc;
    --paper:#ffffff;
    --red:#d63a40;
    --coral:#ee6a6e;
    --rose:#f4a3a5;
    --blush:#fbe4e4;
    --blush-soft:rgba(236,140,140,.26);
    --ink:#5a4a48;
    --muted:#9b8d8a;
    --line:#e6dada;
  }
  *{box-sizing:border-box;margin:0;padding:0}
  html,body{width:1200px;height:308px;overflow:hidden}
  body{background:var(--bg);font-family:"Open Sans",sans-serif;color:var(--ink);position:relative}
  .piece{position:absolute;background:var(--paper);box-shadow:0 2px 5px rgba(0,0,0,.16);overflow:hidden}
  .brand{font-family:"Pacifico",cursive;color:var(--red);white-space:nowrap;line-height:1}
  .brand-dot{display:inline-block;border-radius:50%;background:var(--red);vertical-align:middle}
  .watermark{position:absolute;border-radius:50%;background:radial-gradient(circle,var(--blush-soft) 0%,rgba(251,228,228,0) 70%)}

  /* master logo */
  .master{position:absolute;left:14px;top:20px;width:280px}
  .master .brand{font-size:15px}
  .master .brand-dot{width:12px;height:12px;margin-right:5px}
  .master .tagline{font-size:6px;color:var(--muted);margin-top:6px;padding-left:18px}

  /* business cards */
  .card{width:140px;height:58px}
  .card .brand{position:absolute;left:8px;top:8px;font-size:7px}
  .card .brand-dot{width:6px;height:6px;margin-right:3px}
  .card .person{position:absolute;right:8px;bottom:9px;text-align:right;font-size:4.5px;line-height:1.4;color:var(--ink)}
  .card .person strong{display:block;font-size:5.5px;font-weight:600;color:var(--red)}
  .card .band{position:absolute;left:0;right:0;bottom:0;height:4px;background:var(--rose)}
  .card--1{left:10px;top:104px}
  .card--2{left:156px;top:104px}
  .card--3{left:10px;top:168px}
  .card--4{left:156px;top:168px}
  .card--5{left:10px;top:232px}
  .card--back{left:156px;top:232px;background:var(--blush)}
  .card--back .pitch{position:absolute;left:10px;top:8px;color:var(--ink);font-size:4.5px;line-height:1.55}
  .card--back .pitch b{display:block;font-size:6px;font-weight:600;color:var(--red);margin-bottom:2px}
  .card--back .watermark{right:-10px;top:-6px;width:70px;height:70px;background:radial-gradient(circle,rgba(214,58,64,.16) 0%,rgba(214,58,64,0) 70%)}

  /* letterheads */
  .letter{width:150px;height:214px;top:20px}
  .letter--one{left:320px}
  .letter--two{left:488px}
  .letter .brand{position:absolute;left:50%;top:12px;transform:translateX(-50%);font-size:8px}
  .letter .brand-dot{width:6px;height:6px;margin-right:3px}
  .letter--one .brand{left:10px;transform:none}
  .letter .contact{position:absolute;right:10px;top:10px;text-align:right;font-size:3.5px;line-height:1.4;color:var(--muted)}
  .letter .watermark{left:20px;top:50px;width:110px;height:110px}
  .letter .footer{position:absolute;left:0;right:0;bottom:0;height:10px;background:var(--blush);color:var(--red);font-size:4px;text-align:center;line-height:10px}

  /* small envelopes */
  .env-small{width:156px;height:96px;left:660px}
  .env-small--top{top:48px}
  .env-small--bottom{top:176px}
  .env-small .brand{position:absolute;left:10px;top:10px;font-size:7px}
  .env-small .brand-dot{width:6px;height:6px;margin-right:3px}
  .env-small .watermark{left:50px;top:10px;width:80px;height:80px}
  .env-small .stamp{position:absolute;right:8px;top:8px;width:18px;height:20px;border:1px dashed var(--muted);font-size:3.5px;text-align:center;line-height:18px;color:var(--muted)}
  .env-small .strip{position:absolute;left:0;right:0;bottom:0;height:6px;background:var(--rose)}

  /* large envelopes */
  .env-large{width:282px;height:124px;left:846px}
  .env-large--colour{top:46px}
  .env-large--plain{top:186px;height:100px}
  .env-large svg{position:absolute;inset:0}
  .env-large .brand{position:absolute;left:50%;top:62px;transform:translateX(-50%);font-size:10px}
  .env-large .brand-dot{width:8px;height:8px;margin-right:4px}
</style>
</head>
<body>

<section class="master">
  <div class="brand"><span class="brand-dot"></span>Wander Glade Journeys</div>
  <div class="tagline">Dream trips made simple</div>
</section>

<article class="piece card card--1">
  <div class="brand"><span class="brand-dot"></span>Wander Glade Journeys</div>
  <div class="person"><strong>Nora Pell</strong>Travel Consultant<br>555.204.7719 · 555.316.8245<br>nora.pell@wanderglade.example</div>
  <div class="band"></div>
</article>

<article class="piece card card--2">
  <div class="brand"><span class="brand-dot"></span>Wander Glade Journeys</div>
  <div class="person"><strong>Glen Ashby</strong>Marketing Director<br>555.204.7719 · 555.316.8245<br>glen.ashby@wanderglade.example</div>
  <div class="band"></div>
</article>

<article class="piece card card--3">
  <div class="brand"><span class="brand-dot"></span>Wander Glade Journeys</div>
  <div class="person"><strong>Tessa Vandrunen</strong>Travel Consultant<br>555.204.7719 · 555.316.8245<br>tessa.vandrunen@wanderglade.example</div>
  <div class="band"></div>
</article>

<article class="piece card card--4">
  <div class="brand"><span class="brand-dot"></span>Wander Glade Journeys</div>
  <div class="person"><strong>Megan Tully</strong>Travel Consultant<br>555.204.7719 · 555.316.8245<br>megan.tully@wanderglade.example</div>
  <div class="band"></div>
</article>

<article class="piece card card--5">
  <div class="brand"><span class="brand-dot"></span>Wander Glade Journeys</div>
  <div class="person"><strong>Jodi Farley</strong>Travel Consultant<br>555.204.7719 · 555.316.8245<br>jodi.farley@wanderglade.example</div>
  <div class="band"></div>
</article>

<article class="piece card card--back">
  <div class="watermark" role="img" aria-label="Faded heart artwork"></div>
  <div class="pitch"><b>Where can we take you?</b>Honeymoons<br>Destination Weddings<br>Family Travel<br>Celebration Vacations</div>
</article>

<article class="piece letter letter--one">
  <div class="brand"><span class="brand-dot"></span>Wander Glade Journeys</div>
  <div class="contact">555.204.7719<br>555.316.8245<br>wanderglade.example</div>
  <div class="watermark" role="img" aria-label="Faded heart artwork"></div>
</article>

<article class="piece letter letter--two">
  <div class="brand"><span class="brand-dot"></span>Wander Glade Journeys</div>
  <div class="watermark" role="img" aria-label="Faded heart artwork"></div>
  <div class="footer">555.204.7719 · wanderglade.example</div>
</article>

<article class="piece env-small env-small--top">
  <div class="brand"><span class="brand-dot"></span>Wander Glade Journeys</div>
  <div class="watermark" role="img" aria-label="Faded heart artwork"></div>
  <div class="stamp">Postage</div>
</article>

<article class="piece env-small env-small--bottom">
  <div class="brand"><span class="brand-dot"></span>Wander Glade Journeys</div>
  <div class="strip"></div>
</article>

<article class="piece env-large env-large--colour">
  <svg width="282" height="124" viewBox="0 0 282 124">
    <defs>
      <linearGradient id="flap" x1="0" y1="0" x2="0" y2="1">
        <stop offset="0" stop-color="#ee6a6e"/>
        <stop offset="1" stop-color="#f7b3b4"/>
      </linearGradient>
    </defs>
    <path d="M0 0 L282 0 L141 54 Z" fill="url(#flap)"/>
    <path d="M0 124 L141 70 L282 124" fill="none" stroke="#e9dede" stroke-width="1"/>
  </svg>
  <div class="brand"><span class="brand-dot"></span>Wander Glade Journeys</div>
</article>

<article class="piece env-large env-large--plain">
  <svg width="282" height="100" viewBox="0 0 282 100">
    <path d="M0 0 L141 48 L282 0" fill="none" stroke="#d9cfcf" stroke-width="1"/>
    <path d="M0 100 L141 52 L282 100" fill="none" stroke="#e9dede" stroke-width="1"/>
  </svg>
</article>

</body>
</html>
```